Mirova Coffee Beans

I need a label design for our coffee beans brand. The labels would be stuck on a neutral black valve packaging. The labels have a size of 10 × 20 cm.
1 variety: Café Tramo 60/40
2 variety: Café Sorrel 70/30
3 variety: Café Tiva 80/20
4 variety: Café Wisp 100%
5 varieties: Espresso Vasto 50/50
6 varieties: Espresso Calmora 60/40
7 variety: Espresso Nevio 80/20
8 variety: Brisa Kalumetos (specially roasted for Freddo Espresso / Cappuccino)

For example, 70/30 means 70%Arabica 30%Robusta

every label must say: www.tessuna.de Tessuna
Lindenkamp-Weg-Str. 7
47618 Hallendorf, whole roasted coffee beans, store in a cool dry place , But in german (www.tessuna.de Tessuna
Lindenkamp-Weg-Str. 7
47618 Hallendorf, whole coffee beans roasted, store in a cool, dry place)

the labels should be plain and all in a different color

Target Market(s)

Coffee beans

Requirements
Must have
• our logo see attachment! the coffee varieties white label black writing! the espresso varieties black label white writing!
Nice to have
• Modern, perhaps with numbers like 70/30 on a large scale
Should not have
• characters

```html
<!DOCTYPE html>
<html lang="de">
<head>
<meta charset="utf-8">
<title>Tessuna – Etiketten Kaffeebohnen</title>
<link rel="stylesheet" href="https://fonts.googleapis.com/css2?family=Montserrat:wght@300;400;500;600;700&family=Barlow:wght@500&display=swap">
<style>
  :root{
    --canvas:#e9e9e9;
    --paper:#ffffff;
    --ink:#1d1d1d;
    --night:#050505;
    --snow:#ffffff;
    --tramo:#f9d7b5;
    --sorrel:#946740;
    --tiva:#d99a62;
    --wisp:#a28b00;
    --vasto:#8593a7;
    --calmora:#a48c00;
    --nevio:#1a6c24;
    --brisa:#6a1c57;
  }
  *{box-sizing:border-box;margin:0;padding:0}
  html,body{width:1200px;height:1200px;overflow:hidden;background:var(--canvas)}
  body{font-family:"Montserrat",sans-serif}
  .label-sheet{
    width:1200px;height:1200px;
    display:grid;
    grid-template-columns:repeat(4,240px);
    grid-template-rows:repeat(2,480px);
    column-gap:48px;row-gap:80px;
    padding:80px 48px;
  }
  .label{
    position:relative;width:240px;height:480px;
    background:var(--paper);color:var(--ink);
  }
  .label--espresso{background:var(--night);color:var(--snow)}
  .brand{
    position:absolute;top:28px;left:0;right:0;text-align:center;
    font-size:29px;font-weight:400;letter-spacing:1px;
  }
  .brand-cup{
    position:absolute;top:76px;left:112px;width:16px;height:14px;
    border-radius:0 0 8px 8px;
    background:linear-gradient(#8a5a35,#3b2414);
  }
  .brand-rule{
    position:absolute;top:94px;left:45px;width:150px;height:1px;background:currentColor;
  }
  .variety{
    position:absolute;top:159px;left:0;width:240px;height:29px;
    font-family:"Barlow",sans-serif;font-weight:500;font-size:20px;
    text-align:center;line-height:30px;letter-spacing:.3px;text-transform:uppercase;
  }
  .label--coffee .variety{color:var(--ink)}
  .label--espresso .variety{color:var(--snow)}
  .variety--tramo{background:var(--tramo)}
  .variety--sorrel{background:var(--sorrel)}
  .variety--tiva{background:var(--tiva)}
  .variety--wisp{background:var(--wisp)}
  .variety--vasto{background:var(--vasto)}
  .variety--calmora{background:var(--calmora)}
  .variety--nevio{background:var(--nevio)}
  .variety--brisa{background:var(--brisa)}
  .blend{position:absolute;top:308px;left:17px}
  .blend-ratio{font-size:20px;font-weight:400;letter-spacing:1px;line-height:24px}
  .blend-note{font-size:6.5px;font-weight:400;letter-spacing:.3px;margin-top:2px;text-transform:uppercase}
  .blend-ratio--claim{font-size:13px;letter-spacing:.6px;line-height:18px;text-transform:uppercase}
  .product-type{
    position:absolute;top:419px;left:19px;display:flex;align-items:center;gap:3px;
    font-size:6.5px;font-weight:700;letter-spacing:.8px;line-height:8px;text-transform:uppercase;
  }
  .product-type svg{width:20px;height:12px}
  .address{
    position:absolute;top:447px;left:19px;font-size:4.5px;line-height:5.5px;letter-spacing:.2px;
  }
  .website{
    position:absolute;top:460px;left:19px;font-size:9px;font-weight:500;
  }
  .net-weight{
    position:absolute;top:436px;right:14px;text-align:right;
  }
  .net-weight-value{font-size:21px;font-weight:400;line-height:22px}
  .net-weight-value small{font-size:17px;font-weight:300;margin-right:1px}
  .storage{font-size:6.5px;font-weight:500;margin-top:1px}
</style>
</head>
<body>
<main class="label-sheet">

  <article class="label label--coffee">
    <div class="brand">TESSUNA</div>
    <div class="brand-cup" role="img" aria-label="Kleine Kaffeetasse"></div>
    <div class="brand-rule"></div>
    <h2 class="variety variety--tramo">Café Tramo</h2>
    <div class="blend"><p class="blend-ratio">60/40</p><p class="blend-note">60%Arabica | 40%Robusta</p></div>
    <p class="product-type"><svg viewBox="0 0 20 12"><ellipse cx="5.5" cy="6" rx="4.5" ry="5.5" fill="currentColor"/><ellipse cx="14.5" cy="6" rx="4.5" ry="5.5" fill="currentColor"/></svg>Ganze geröstete<br>Kaffeebohnen</p>
    <p class="address">Lindenkamp-Weg-Str. 7<br>47618 Hallendorf</p>
    <p class="website">www.tessuna.de</p>
    <div class="net-weight"><p class="net-weight-value"><small>e</small>1000 g</p><p class="storage">Kühl und trocken lagern</p></div>
  </article>

  <article class="label label--coffee">
    <div class="brand">TESSUNA</div>
    <div class="brand-cup" role="img" aria-label="Kleine Kaffeetasse"></div>
    <div class="brand-rule"></div>
    <h2 class="variety variety--sorrel">Café Sorrel</h2>
    <div class="blend"><p class="blend-ratio">70/30</p><p class="blend-note">70%Arabica | 30%Robusta</p></div>
    <p class="product-type"><svg viewBox="0 0 20 12"><ellipse cx="5.5" cy="6" rx="4.5" ry="5.5" fill="currentColor"/><ellipse cx="14.5" cy="6" rx="4.5" ry="5.5" fill="currentColor"/></svg>Ganze geröstete<br>Kaffeebohnen</p>
    <p class="address">Lindenkamp-Weg-Str. 7<br>47618 Hallendorf</p>
    <p class="website">www.tessuna.de</p>
    <div class="net-weight"><p class="net-weight-value"><small>e</small>1000 g</p><p class="storage">Kühl und trocken lagern</p></div>
  </article>

  <article class="label label--coffee">
    <div class="brand">TESSUNA</div>
    <div class="brand-cup" role="img" aria-label="Kleine Kaffeetasse"></div>
    <div class="brand-rule"></div>
    <h2 class="variety variety--tiva">Café Tiva</h2>
    <div class="blend"><p class="blend-ratio">80/20</p><p class="blend-note">80%Arabica | 20%Robusta</p></div>
    <p class="product-type"><svg viewBox="0 0 20 12"><ellipse cx="5.5" cy="6" rx="4.5" ry="5.5" fill="currentColor"/><ellipse cx="14.5" cy="6" rx="4.5" ry="5.5" fill="currentColor"/></svg>Ganze geröstete<br>Kaffeebohnen</p>
    <p class="address">Lindenkamp-Weg-Str. 7<br>47618 Hallendorf</p>
    <p class="website">www.tessuna.de</p>
    <div class="net-weight"><p class="net-weight-value"><small>e</small>1000 g</p><p class="storage">Kühl und trocken lagern</p></div>
  </article>

  <article class="label label--coffee">
    <div class="brand">TESSUNA</div>
    <div class="brand-cup" role="img" aria-label="Kleine Kaffeetasse"></div>
    <div class="brand-rule"></div>
    <h2 class="variety variety--wisp">Café Wisp</h2>
    <div class="blend"><p class="blend-ratio">100%</p><p class="blend-note">100%Arabica</p></div>
    <p class="product-type"><svg viewBox="0 0 20 12"><ellipse cx="5.5" cy="6" rx="4.5" ry="5.5" fill="currentColor"/><ellipse cx="14.5" cy="6" rx="4.5" ry="5.5" fill="currentColor"/></svg>Ganze geröstete<br>Kaffeebohnen</p>
    <p class="address">Lindenkamp-Weg-Str. 7<br>47618 Hallendorf</p>
    <p class="website">www.tessuna.de</p>
    <div class="net-weight"><p class="net-weight-value"><small>e</small>1000 g</p><p class="storage">Kühl und trocken lagern</p></div>
  </article>

  <article class="label label--espresso">
    <div class="brand">TESSUNA</div>
    <div class="brand-cup" role="img" aria-label="Kleine Kaffeetasse"></div>
    <div class="brand-rule"></div>
    <h2 class="variety variety--vasto">Espresso Vasto</h2>
    <div class="blend"><p class="blend-ratio">50/50</p><p class="blend-note">50%Arabica | 50%Robusta</p></div>
    <p class="product-type"><svg viewBox="0 0 20 12"><ellipse cx="5.5" cy="6" rx="4.5" ry="5.5" fill="currentColor"/><ellipse cx="14.5" cy="6" rx="4.5" ry="5.5" fill="currentColor"/></svg>Ganze geröstete<br>Kaffeebohnen</p>
    <p class="address">Lindenkamp-Weg-Str. 7<br>47618 Hallendorf</p>
    <p class="website">www.tessuna.de</p>
    <div class="net-weight"><p class="net-weight-value"><small>e</small>1000 g</p><p class="storage">Kühl und trocken lagern</p></div>
  </article>

  <article class="label label--espresso">
    <div class="brand">TESSUNA</div>
    <div class="brand-cup" role="img" aria-label="Kleine Kaffeetasse"></div>
    <div class="brand-rule"></div>
    <h2 class="variety variety--calmora">Espresso Calmora</h2>
    <div class="blend"><p class="blend-ratio">60/40</p><p class="blend-note">60%Arabica | 40%Robusta</p></div>
    <p class="product-type"><svg viewBox="0 0 20 12"><ellipse cx="5.5" cy="6" rx="4.5" ry="5.5" fill="currentColor"/><ellipse cx="14.5" cy="6" rx="4.5" ry="5.5" fill="currentColor"/></svg>Ganze geröstete<br>Kaffeebohnen</p>
    <p class="address">Lindenkamp-Weg-Str. 7<br>47618 Hallendorf</p>
    <p class="website">www.tessuna.de</p>
    <div class="net-weight"><p class="net-weight-value"><small>e</small>1000 g</p><p class="storage">Kühl und trocken lagern</p></div>
  </article>

  <article class="label label--espresso">
    <div class="brand">TESSUNA</div>
    <div class="brand-cup" role="img" aria-label="Kleine Kaffeetasse"></div>
    <div class="brand-rule"></div>
    <h2 class="variety variety--nevio">Espresso Nevio</h2>
    <div class="blend"><p class="blend-ratio">80/20</p><p class="blend-note">80%Arabica | 20%Robusta</p></div>
    <p class="product-type"><svg viewBox="0 0 20 12"><ellipse cx="5.5" cy="6" rx="4.5" ry="5.5" fill="currentColor"/><ellipse cx="14.5" cy="6" rx="4.5" ry="5.5" fill="currentColor"/></svg>Ganze geröstete<br>Kaffeebohnen</p>
    <p class="address">Lindenkamp-Weg-Str. 7<br>47618 Hallendorf</p>
    <p class="website">www.tessuna.de</p>
    <div class="net-weight"><p class="net-weight-value"><small>e</small>1000 g</p><p class="storage">Kühl und trocken lagern</p></div>
  </article>

  <article class="label label--espresso">
    <div class="brand">TESSUNA</div>
    <div class="brand-cup" role="img" aria-label="Kleine Kaffeetasse"></div>
    <div class="brand-rule"></div>
    <h2 class="variety variety--brisa">Brisa Kalumetos</h2>
    <div class="blend"><p class="blend-ratio blend-ratio--claim">Specially roasted for</p><p class="blend-note">Freddo Espresso / Cappuccino)</p></div>
    <p class="product-type"><svg viewBox="0 0 20 12"><ellipse cx="5.5" cy="6" rx="4.5" ry="5.5" fill="currentColor"/><ellipse cx="14.5" cy="6" rx="4.5" ry="5.5" fill="currentColor"/></svg>Ganze geröstete<br>Kaffeebohnen</p>
    <p class="address">Lindenkamp-Weg-Str. 7<br>47618 Hallendorf</p>
    <p class="website">www.tessuna.de</p>
    <div class="net-weight"><p class="net-weight-value"><small>e</small>1000 g</p><p class="storage">Kühl und trocken lagern</p></div>
  </article>

</main>
</body>
</html>
```